Strategic Planning Process

To create an infographic overviewing our strategic planning process

This is a one page infographic, portrait or landscape. Ideal size is something that fits on 8.5 by 11 paper.

I want to give designers an extra day or two to create designs. My project description was unclear.

The visual elements selection on the draft was added to offer suggestions on what to include on the infographic, not to be literally included on the infographic

```html
<!DOCTYPE html>
<html lang="en">
<head>
<meta charset="utf-8">
<title>Achieving Strategic Alignment – Five-Step Process</title>
<link rel="stylesheet" href="https://fonts.googleapis.com/css2?family=Oswald:wght@500;600&family=Poppins:wght@400&display=swap">
<style>
  :root {
    --navy: #2c2a6b;
    --gold: #b8955a;
    --paper: #ffffff;
    --map-tone: #eceef1;
    --badge-bg: #ffffff;
  }
  * { margin: 0; padding: 0; box-sizing: border-box; }
  html, body { width: 1200px; height: 846px; overflow: hidden; background: var(--paper); }
  .canvas { position: relative; width: 1200px; height: 846px; overflow: hidden; background: var(--paper); font-family: "Oswald", sans-serif; }

  .world-map {
    position: absolute; left: 60px; top: 175px; width: 1085px; height: 575px;
    background: radial-gradient(ellipse at 50% 45%, var(--map-tone) 0%, #f4f5f7 55%, rgba(255,255,255,0) 80%);
    border-radius: 40%;
  }

  .headline { position: absolute; left: 83px; top: 58px; font-size: 46px; font-weight: 600; letter-spacing: 1px; line-height: 1; white-space: nowrap; }
  .headline .accent { color: var(--gold); }
  .headline .main { color: var(--navy); }

  .brand-name { position: absolute; right: 50px; top: 80px; color: var(--navy); font-weight: 600; font-size: 28px; line-height: 1; letter-spacing: 1px; white-space: nowrap; }

  .process-diagram { position: absolute; left: 0; top: 0; width: 1200px; height: 846px; }

  .step-label { position: absolute; color: var(--navy); font-weight: 600; font-size: 27px; letter-spacing: 1px; line-height: 1; white-space: nowrap; }
  .step-envision { left: 278px; top: 224px; }
  .step-discover { left: 792px; top: 224px; }
  .step-reveal { left: 870px; top: 469px; }
  .step-reimagine { left: 526px; top: 688px; }
  .step-actualize { left: 190px; top: 469px; }

  .process-title { position: absolute; left: 442px; top: 345px; width: 300px; text-align: center; font-weight: 600; line-height: 1; white-space: nowrap; }
  .process-title .count { display: block; color: var(--gold); font-size: 56px; }
  .process-title .word { display: block; color: var(--navy); font-size: 64px; margin-top: 6px; }

  .footer-band { position: absolute; left: 0; bottom: 0; width: 1200px; height: 95px; }
  .footer-url { position: absolute; left: 0; bottom: 22px; width: 1200px; text-align: center; color: #ffffff; font-family: "Poppins", sans-serif; font-size: 21px; }
</style>
</head>
<body>
<main class="canvas">
  <div class="world-map" role="img" aria-label="Faint dotted world map in the background"></div>

  <h1 class="headline"><span class="accent">ACHIEVING</span> <span class="main">STRATEGIC ALIGNMENT</span></h1>

  <p class="brand-name">ORVANTHE PARTNERS</p>

  <svg class="process-diagram" viewBox="0 0 1200 846" aria-hidden="true">
    <defs>
      <marker id="arrow-head" viewBox="0 0 10 10" refX="6" refY="5" markerWidth="5" markerHeight="5" orient="auto">
        <path d="M0 0 L10 5 L0 10 Z" fill="var(--navy)"/>
      </marker>
      <g id="step-node">
        <circle r="45" fill="none" stroke="var(--navy)" stroke-width="4"/>
        <circle r="38" fill="none" stroke="var(--gold)" stroke-width="4"/>
        <circle r="33" fill="var(--navy)"/>
      </g>
    </defs>

    <g class="cycle-arrows" fill="none" stroke="var(--navy)" stroke-width="7" stroke-linecap="round" marker-end="url(#arrow-head)">
      <path d="M548 202 Q598 182 648 198"/>
      <path d="M765 295 Q802 330 800 392"/>
      <path d="M748 548 Q722 592 676 606"/>
      <path d="M525 590 Q470 592 435 545"/>
      <path d="M392 410 Q386 352 420 300"/>
    </g>

    <g class="step-nodes">
      <use href="#step-node" x="472" y="238"/>
      <use href="#step-node" x="717" y="240"/>
      <use href="#step-node" x="787" y="472"/>
      <use href="#step-node" x="595" y="615"/>
      <use href="#step-node" x="393" y="470"/>
    </g>

    <g class="step-icons" fill="none" stroke="var(--gold)" stroke-width="2.5" stroke-linecap="round" stroke-linejoin="round">
      <g transform="translate(472 238)">
        <circle r="8"/><circle r="15" stroke-dasharray="5 4"/>
      </g>
      <g transform="translate(717 240)">
        <path d="M-6 8 h12 M-5 12 h10 M-7 4 a10 10 0 1 1 14 0"/>
      </g>
      <g transform="translate(787 472)">
        <rect x="-13" y="-4" width="26" height="17"/><path d="M-7 -10 l4 4 l9 -9"/>
      </g>
      <g transform="translate(595 615)">
        <circle r="13"/><circle r="5"/><path d="M0 -18 v6 M0 12 v6 M-18 0 h6 M12 0 h6"/>
      </g>
      <g transform="translate(393 470)">
        <rect x="-13" y="-15" width="18" height="24"/><path d="M-9 -8 h10 M-9 -2 h10 M-9 4 h6"/><circle cx="8" cy="8" r="7"/>
      </g>
    </g>

    <g class="step-numbers" font-family="Oswald, sans-serif" font-weight="600" font-size="15" fill="var(--navy)" text-anchor="middle">
      <circle cx="472" cy="180" r="12" fill="var(--badge-bg)" stroke="var(--navy)" stroke-width="2.5"/>
      <text x="472" y="186">1</text>
      <circle cx="717" cy="182" r="12" fill="var(--badge-bg)" stroke="var(--navy)" stroke-width="2.5"/>
      <text x="717" y="188">2</text>
      <circle cx="787" cy="413" r="12" fill="var(--badge-bg)" stroke="var(--navy)" stroke-width="2.5"/>
      <text x="787" y="419">3</text>
      <circle cx="595" cy="557" r="12" fill="var(--badge-bg)" stroke="var(--navy)" stroke-width="2.5"/>
      <text x="595" y="563">4</text>
      <circle cx="393" cy="412" r="12" fill="var(--badge-bg)" stroke="var(--navy)" stroke-width="2.5"/>
      <text x="393" y="418">5</text>
    </g>
  </svg>

  <span class="step-label step-envision">ENVISION</span>
  <span class="step-label step-discover">DISCOVER</span>
  <span class="step-label step-reveal">REVEAL</span>
  <span class="step-label step-reimagine">REIMAGINE</span>
  <span class="step-label step-actualize">ACTUALIZE</span>

  <div class="process-title">
    <span class="count">FIVE-STEP</span>
    <span class="word">PROCESS</span>
  </div>

  <svg class="footer-band" viewBox="0 0 1200 95" preserveAspectRatio="none" aria-hidden="true">
    <path d="M0 18 Q150 6 300 14 T600 12 T900 16 T1200 10 V40 H0 Z" fill="var(--gold)"/>
    <path d="M0 30 Q200 20 400 28 T800 26 T1200 24 V95 H0 Z" fill="var(--navy)"/>
  </svg>
  <p class="footer-url">www.orvanthepartners.com</p>
</main>
</body>
</html>
```